Design cover for information booklet
I am looking for a design for the front and back cover of an information booklet. Also an inside page basic design.
The booklet will contain 10 double sided pages providing information on weight loss surgery.
See my website www.brevinmarsh.com.au for what I do and typical colour themes.
I would also like some theming/illustration which can be utilised on each inside page of the booklet, rather than the pages just being blank with text etc. What would a blank page on this inside of the booklet look like under the design theme that you have created?
My company is Kestrel Institute for Metabolic Surgery. You will find uploaded a Logo for Kestrel Institute for Metabolic Surgery as well as my other logo which is my name “Brevin Marsh, etc.”. The Kestrel Institute for Metabolic Surgery logo should be utilised. The other logo (Brevin Marsh) is optional.
The front cover should contain the following text as minimum:
Kestrel Institute for Metabolic Surgery
Mr Brevin Marsh MBBS FRACS GradCert (Health Stats)
Our tagline is “Experience, Expertise and Empathy”. This should probably be on the front cover also.
The back cover contains (as a minimum) our address, phone number, fax number:
Suite 17, Level 3
Tallowgate Northern Hospital
9 Pemberly Road, Fernwick VIC 3174
Phone: 03 9412 6083
Fax: 03 9417 2865
Email: info@kestrelims.com.au
The files should be in a form whereby the text can be edited and changed if need be.
1. problems with initial graphical attachments - Artforge end 2. several requests by designers for extension

```html
<!DOCTYPE html>
<html lang="en">
<head>
<meta charset="utf-8">
<title>Kestrel Institute for Metabolic Surgery – Booklet Covers</title>
<link href="https://fonts.googleapis.com/css2?family=Playfair+Display:wght@400;700&family=Open+Sans:wght@400;600;700&display=swap" rel="stylesheet">
<style>
  :root{
    --teal:#1f8a80;
    --teal-dark:#146a62;
    --teal-light:#7cc2b9;
    --photo-a:#8fb4cf;
    --photo-b:#3f6f8f;
    --grey:#6d6f71;
    --grey-bar:#8a8c8e;
    --ink:#4a4c4e;
    --paper:#ffffff;
    --backdrop:#e4e5e6;
  }
  *{box-sizing:border-box;margin:0;padding:0}
  html,body{width:798px;height:1200px;overflow:hidden;background:var(--backdrop);font-family:"Open Sans",sans-serif}
  .canvas{position:relative;width:798px;height:1200px}

  .page{position:absolute;background:var(--paper);overflow:hidden;box-shadow:0 2px 8px rgba(0,0,0,.12)}
  .front-cover{width:420px;height:594px}
  .front-cover--main{left:189px;top:24px}
  .front-cover--spread{left:399px;top:640px;transform:scale(.857);transform-origin:0 0;box-shadow:none}

  .brand{position:absolute;display:flex;align-items:center;gap:8px}
  .brand__mark{width:34px;height:34px;background:var(--teal)}
  .brand__name{font-family:"Playfair Display",serif;font-weight:700;color:var(--teal);font-size:12px;line-height:1.15;text-transform:uppercase;letter-spacing:.5px}
  .front-cover .brand{left:130px;top:34px}

  .band-svg{position:absolute;left:0;width:100%}
  .cover-photo{position:absolute;left:0;top:118px;width:420px;height:214px;background:linear-gradient(135deg,var(--photo-a),var(--photo-b))}

  .tagline{position:absolute;left:30px;top:352px;font-family:"Playfair Display",serif;font-weight:700;color:var(--teal);font-size:29px;line-height:1.12;text-transform:uppercase}
  .subtitle{position:absolute;left:30px;top:424px;color:var(--grey);font-size:10px}
  .phone-bar{position:absolute;right:0;top:460px;width:150px;height:22px;background:var(--grey-bar);color:#fff;font-size:9px;display:flex;align-items:center;padding-left:14px;gap:6px}
  .web{position:absolute;left:26px;bottom:14px;color:#fff;font-size:10px;display:flex;align-items:center;gap:6px}

  .back-cover{left:39px;top:640px;width:360px;height:509px}
  .back-cover .top-band{position:absolute;left:0;top:0;width:360px;height:26px;background:var(--teal)}
  .back-photo{position:absolute;left:0;top:26px;width:168px;height:140px;background:linear-gradient(135deg,#c9cfd3,#7d8a91)}
  .back-cover .brand--top{left:186px;top:46px}
  .back-cover .brand--top .brand__mark{width:24px;height:24px}
  .back-cover .brand--top .brand__name{font-size:8.5px}
  .section-title{position:absolute;left:186px;top:92px;color:var(--teal);font-family:"Playfair Display",serif;font-size:13px}
  .intro{position:absolute;left:22px;top:186px;width:316px;color:var(--ink);font-size:8.5px;line-height:1.55}
  .doctor-photo{position:absolute;left:128px;top:318px;width:62px;height:78px;background:linear-gradient(160deg,#a9b3b8,#4e5a61)}
  .doctor-info{position:absolute;left:200px;top:318px;width:150px;color:var(--ink);font-size:7px;line-height:1.5}
  .doctor-info strong{color:var(--teal);font-size:7.5px;display:block;margin-bottom:2px}
  .back-cover .brand--foot{left:22px;top:410px}
  .back-cover .brand--foot .brand__mark{width:22px;height:22px}
  .back-cover .brand--foot .brand__name{font-size:7.5px}
  .contact{position:absolute;left:200px;top:406px;color:var(--ink);font-size:7px;line-height:1.55}
  .contact span{color:var(--teal);font-weight:700}
  .back-cover .foot-band{position:absolute;left:0;bottom:0;width:360px;height:30px;background:var(--teal)}
</style>
</head>
<body>
<div class="canvas">

  <section class="page front-cover front-cover--main">
    <div class="brand"><div class="brand__mark"></div><div class="brand__name">Kestrel Institute<br>for Metabolic Surgery</div></div>
    <svg class="band-svg" style="top:96px" width="420" height="24" viewBox="0 0 420 24"><polygon points="0,8 420,0 420,24 0,24" fill="var(--teal)"/></svg>
    <div class="cover-photo" role="img" aria-label="Photo of a surgical team in blue gowns operating"></div>
    <h1 class="tagline">Experience,<br>Expertise &amp; Empathy</h1>
    <p class="subtitle">A patient guide to weight loss surgery</p>
    <div class="phone-bar">
      <svg width="9" height="9" viewBox="0 0 24 24"><path d="M6.6 10.8a15 15 0 0 0 6.6 6.6l2.2-2.2a1 1 0 0 1 1-.25 11.4 11.4 0 0 0 3.6.6 1 1 0 0 1 1 1V20a1 1 0 0 1-1 1A17 17 0 0 1 3 4a1 1 0 0 1 1-1h3.5a1 1 0 0 1 1 1 11.4 11.4 0 0 0 .6 3.6 1 1 0 0 1-.25 1z" fill="#fff"/></svg>
      03 9412 6083
    </div>
    <svg class="band-svg" style="bottom:0" width="420" height="58" viewBox="0 0 420 58"><polygon points="0,14 420,0 420,58 0,58" fill="var(--teal)"/><polygon points="0,14 420,0 420,5 0,19" fill="var(--teal-light)"/></svg>
    <div class="web">www.brevinmarsh.com.au</div>
  </section>

  <section class="page back-cover">
    <div class="top-band"></div>
    <div class="back-photo" role="img" aria-label="Photo of a smiling couple embracing"></div>
    <div class="brand brand--top"><div class="brand__mark"></div><div class="brand__name">Kestrel Institute<br>for Metabolic Surgery</div></div>
    <h2 class="section-title">Welcome to our practice</h2>
    <p class="intro">Our team provides safe, caring weight loss surgery for patients across the region. From first consultation to long term follow up, we guide each person through every stage with clear advice, proven methods and ongoing support to help build a healthier future.</p>
    <div class="doctor-photo" role="img" aria-label="Portrait photo of the surgeon in a suit"></div>
    <div class="doctor-info"><strong>Brevin Marsh</strong>Mr Brevin Marsh MBBS FRACS GradCert (Health Stats)</div>
    <div class="brand brand--foot"><div class="brand__mark"></div><div class="brand__name">Kestrel Institute<br>for Metabolic Surgery</div></div>
    <div class="contact">
      Suite 17, Level 3<br>Tallowgate Northern Hospital<br>9 Pemberly Road, Fernwick VIC 3174<br>
      <span>P</span> 03 9412 6083 &nbsp;<span>F</span> 03 9417 2865<br>
      <span>E</span> info@kestrelims.com.au
    </div>
    <div class="foot-band"></div>
  </section>

  <section class="page front-cover front-cover--spread">
    <div class="brand"><div class="brand__mark"></div><div class="brand__name">Kestrel Institute<br>for Metabolic Surgery</div></div>
    <svg class="band-svg" style="top:96px" width="420" height="24" viewBox="0 0 420 24"><polygon points="0,8 420,0 420,24 0,24" fill="var(--teal)"/></svg>
    <div class="cover-photo" role="img" aria-label="Photo of a surgical team in blue gowns operating"></div>
    <h1 class="tagline">Experience,<br>Expertise &amp; Empathy</h1>
    <p class="subtitle">A patient guide to weight loss surgery</p>
    <div class="phone-bar">
      <svg width="9" height="9" viewBox="0 0 24 24"><path d="M6.6 10.8a15 15 0 0 0 6.6 6.6l2.2-2.2a1 1 0 0 1 1-.25 11.4 11.4 0 0 0 3.6.6 1 1 0 0 1 1 1V20a1 1 0 0 1-1 1A17 17 0 0 1 3 4a1 1 0 0 1 1-1h3.5a1 1 0 0 1 1 1 11.4 11.4 0 0 0 .6 3.6 1 1 0 0 1-.25 1z" fill="#fff"/></svg>
      03 9412 6083
    </div>
    <svg class="band-svg" style="bottom:0" width="420" height="58" viewBox="0 0 420 58"><polygon points="0,14 420,0 420,58 0,58" fill="var(--teal)"/><polygon points="0,14 420,0 420,5 0,19" fill="var(--teal-light)"/></svg>
    <div class="web">www.brevinmarsh.com.au</div>
  </section>

</div>
</body>
</html>
```